Rigging Brochure for New Electric Crane!!!

We have purchased a new Veltra crane from Italy that will arrive in March 2020. We would like to advertise that we will be the only company in North America with this crane. This will be the highlight of the brochure.
We would also like a section that shows our other services, such as machinery moving, transportation, warehouse storage, government work etc.

We are interested in purchasing more than one design and are open to both bi-fold and tri-fold brochures.

For a bi-fold the pre-fold size is 17 x 11" so the final size of each section would be 8.5 x 11 inches.
For a tri-fold the pre-fold size would be 11 x 8.5" so each section would be 3.6 x 8.5 inches.

Target Market(s)

Industrial - power plants, machine shops, hospitals, anyone with heavy equipment that needs to be moved or stored

Font styles to use
Sans Serif

Colors
ec1f27
0255a3
ffffff

Requirements
Must have
• Main photo of Veltra crane photoshopped with our company logo on front page
• Our logo and website/contact information
• hollandhoist.example 480-555-0172
Nice to have
• pleasing arrangement of photos that create an overall professional appeal
• company colors of red, white, black, grey and blue
• social media info
• Not all photos need to be used
Should not have
• any competitor's names. All photos provided by Veltra may keep the veltra logo, but any other competitor logos need to be photoshopped out.

```html
<!DOCTYPE html>
<html lang="en">
<head>
<meta charset="utf-8">
<title>Holland Hoist – Veltra Electric Crane Brochure</title>
<link rel="stylesheet" href="https://fonts.googleapis.com/css2?family=Montserrat:wght@400;500;600;700&display=swap">
<style>
  :root {
    --red: #d21c2b;
    --black: #050505;
    --white: #ffffff;
    --paper: #f4f4f4;
    --ink: #2a2a2a;
    --backdrop: #d3d3d3;
  }
  * { box-sizing: border-box; margin: 0; padding: 0; }
  html, body { width: 1200px; height: 943px; overflow: hidden; }
  body {
    background: var(--backdrop);
    font-family: "Montserrat", Arial, sans-serif;
    position: relative;
  }
  .spread {
    position: absolute;
    left: 50px; top: 115px;
    width: 1100px; height: 712px;
    display: flex;
    box-shadow: 0 18px 40px rgba(0,0,0,.22);
  }
  .page { position: relative; width: 550px; height: 712px; overflow: hidden; }
  .page-shapes { position: absolute; inset: 0; }

  /* Left page */
  .page--feature { background: var(--black); }
  .feature-copy {
    position: absolute; left: 44px; top: 34px; width: 470px;
    color: var(--white); font-size: 12.5px; line-height: 1.35;
  }
  .feature-copy p { margin-bottom: 14px; }
  .feature-copy p:nth-child(2) { padding-left: 8px; }
  .feature-copy p:nth-child(3),
  .feature-copy p:nth-child(4) { padding-left: 18px; }
  .feature-copy strong { font-weight: 700; }

  /* Right page */
  .page--services { background: var(--paper); }
  .services-intro {
    position: absolute; left: 30px; top: 26px; width: 300px;
    color: var(--white); font-size: 12px; line-height: 1.35;
  }
  .services-intro h2 { font-size: 12.5px; font-weight: 700; margin-bottom: 14px; }
  .service-list { position: absolute; left: 0; top: 228px; width: 550px; }
  .service {
    position: relative; height: 92px;
    display: flex; align-items: flex-start;
  }
  .service:nth-child(1) { padding-left: 26px; }
  .service:nth-child(2) { padding-left: 48px; }
  .service:nth-child(3) { padding-left: 70px; }
  .service:nth-child(4) { padding-left: 92px; }
  .service:nth-child(5) { padding-left: 114px; }
  .service-photo { position: relative; width: 128px; height: 72px; flex: none; margin-top: 8px; }
  .service-photo::before {
    content: ""; position: absolute; left: -7px; top: -7px;
    width: 80px; height: 60px; background: var(--red);
  }
  .service-photo__fill { position: absolute; inset: 0; }
  .service-text { margin-left: 14px; width: 290px; }
  .service-text h3 {
    color: var(--red); font-size: 12.5px; font-weight: 600;
    text-transform: uppercase; letter-spacing: .2px; margin-bottom: 3px;
  }
  .service-text p { color: var(--ink); font-size: 10.5px; line-height: 1.35; }
</style>
</head>
<body>
<main class="spread">

  <section class="page page--feature">
    <svg class="page-shapes" viewBox="0 0 550 712" width="550" height="712">
      <defs>
        <linearGradient id="craneTone" x1="0" y1="0" x2="1" y2="1">
          <stop offset="0" stop-color="#aeb6bf"/>
          <stop offset=".45" stop-color="#d9d9d9"/>
          <stop offset=".75" stop-color="#c8323a"/>
          <stop offset="1" stop-color="#4a4a4a"/>
        </linearGradient>
      </defs>
      <polygon points="30,320 250,262 360,300 370,252 550,258 550,450" fill="var(--red)"/>
      <polygon points="0,330 30,320 550,470 550,712 0,712" fill="url(#craneTone)"
               role="img" aria-label="Photo of two Veltra electric cranes with raised booms parked beside an industrial building"/>
    </svg>
    <div class="feature-copy">
      <p>The Veltra is safe to use indoors in a clean environment - <strong>it is completely electric. Zero Emissions.</strong></p>
      <p>The Veltra boasts a very tight turning radius that fits in small spaces. The steering radius is as limited as possible because the crane rotates on itself thanks to two slewing bearing units positioned in the rear wheels; the hydro-pneumatic suspensions system assures a perfect distribution of the load on the rear wheels.</p>
      <p>Our <strong>fork fixture</strong> converts the Veltra into a 26T reach lift saving you time and money.</p>
      <p><strong>Got heavy equipment?</strong> We have the equipment and the expertise to lighten your load!</p>
    </div>
  </section>

  <section class="page page--services">
    <svg class="page-shapes" viewBox="0 0 550 712" width="550" height="712">
      <polygon points="0,0 550,0 550,50 0,232" fill="var(--red)"/>
      <polygon points="0,0 470,0 470,30 0,210" fill="var(--black)"/>
    </svg>
    <div class="services-intro">
      <h2>Holland Hoist offers :</h2>
      <p>Machinery Moving, Rigging, Transportation, Packing and Crating Services and Warehouse Storage.</p>
    </div>

    <div class="service-list">
      <article class="service">
        <div class="service-photo"><svg class="service-photo__fill" viewBox="0 0 128 72" role="img" aria-label="Photo of a yellow heavy-haul truck"><rect width="128" height="72" fill="#c9a23a"/><rect y="40" width="128" height="32" fill="#6c6f73"/></svg></div>
        <div class="service-text">
          <h3>Machinery Moving</h3>
          <p>Installation, removal, and relocation of your heavy equipment! All types of equipment including medical, electrical, manufacturing, and industrial.</p>
        </div>
      </article>
      <article class="service">
        <div class="service-photo"><svg class="service-photo__fill" viewBox="0 0 128 72" role="img" aria-label="Photo of a crane loading machinery onto a trailer"><rect width="128" height="72" fill="#b8c2cc"/><rect y="36" width="128" height="36" fill="#3f7d9c"/></svg></div>
        <div class="service-text">
          <h3>Transportation</h3>
          <p>We provide the truck, trailer, riggers, forklift and other necessary equipment to help you transport your machinery or heavy equipment. Packing and Crating services are also available.</p>
        </div>
      </article>
      <article class="service">
        <div class="service-photo"><svg class="service-photo__fill" viewBox="0 0 128 72" role="img" aria-label="Photo of a rigger in safety gear working on plant equipment"><rect width="128" height="72" fill="#4d6b4a"/><rect x="50" width="40" height="72" fill="#c9d94a"/></svg></div>
        <div class="service-text">
          <h3>Utilities</h3>
          <p>Holland Hoist provides power plant outage support. We also rig transformer components for on-site rebuilding. We can install and remove switchgear, breakers, bushings and other plant equipment.</p>
        </div>
      </article>
      <article class="service">
        <div class="service-photo"><svg class="service-photo__fill" viewBox="0 0 128 72" role="img" aria-label="Photo of a forklift beside crated equipment in a yard"><rect width="128" height="72" fill="#8a8476"/><rect y="44" width="128" height="28" fill="#3a3a3a"/></svg></div>
        <div class="service-text">
          <h3>Warehouse Storage</h3>
          <p>Dock level and ground level access to secure warehouse storage for your equipment. Short term and long term storage available.</p>
        </div>
      </article>
      <article class="service">
        <div class="service-photo"><svg class="service-photo__fill" viewBox="0 0 128 72" role="img" aria-label="Photo of a blue crane truck at an industrial site"><rect width="128" height="72" fill="#7a6a55"/><rect x="50" y="10" width="78" height="50" fill="#2e5fa8"/></svg></div>
        <div class="service-text">
          <h3>Emergency Services</h3>
          <p>We offer 24 hour emergency services to get you back up and running! Need a transformer, generator or another piece of necessary equipment replaced or delivered right now? We are here for you!</p>
        </div>
      </article>
    </div>
  </section>

</main>
</body>
</html>
```